■依頼の目的/概要
ハルカゼのlumoraで電子書籍出版をします。

■本の内容
40代女性で話すことや伝えること
自分に自信はないけれど

起業したい、
夢や目標を叶えたい、
という方がターゲットです。

声と潜在意識(心)の力を使う「ひだまりトーン」で
人前で自信をもって伝えられるようになったり
やりたいことがどんどん実現できるようになる方法を
書きました。

声や潜在意識を使ったトレーニング、
実例を用いてお伝えしています。

■デザイン要望
40代女性が好むデザインが希望です。
顔写真も入れていただけたらと思います。
その際、手に持っている音符などは載せないようお願いいたします。

お写真と、電子書籍の文章をお送りいたします。

ご応募、心よりお待ちしております!!!

その他何かご不明な点がございましたら、お気軽にご質問下さい。
よろしくお願いいたします。
タイトルは
響きの名手がひもとく
輝く毎日をつくる心の整え方・磨き方
~ひだまりトーンの秘密~

著者は
ひだまりトーンコンサルタント
さとうれな

どうぞよろしくお願いいたします。
LQS表記では、表紙画像のサイズは 50 MB 未満表紙フ
ァイルの理想的な寸法は 2,560 x 1,600 ピクセルとなっています。

文字が見やすいこと。
女性的な優しいイメージと内容が合うもの、
という視点で選ばせていただきました。

素晴らしい作品ばかりで
選ばせていただくのに時間がかかりました。

短期間にも関わらず
素敵な作品を沢山ご応募いただき
どうもありがとうございました!

心より感謝いたします。

機会がございましたら
またどうぞよろしくお願いいたします。

```html
<!DOCTYPE html>
<html lang="ja">
<head>
<meta charset="utf-8">
<title>輝く毎日をつくる心の整え方・磨き方</title>
<link rel="stylesheet" href="https://fonts.googleapis.com/css2?family=Zen+Maru+Gothic:wght@500;700;900&family=M+PLUS+1p:wght@500;700;800&display=swap">
<style>
  :root {
    --stripe: #dcebf5;
    --paper: #ffffff;
    --accent: #e03a5c;
    --ink: #262626;
    --muted: #6b6b6b;
    --panel: rgba(255,255,255,0.92);
    --photo-a: #f3e2d8;
    --photo-b: #d9b8a8;
  }
  html, body { margin: 0; padding: 0; overflow: hidden; }
  body { width: 750px; height: 1200px; }
  .cover {
    position: relative;
    width: 750px; height: 1200px; overflow: hidden;
    background: repeating-linear-gradient(135deg, var(--paper) 0 14px, var(--stripe) 14px 28px);
    font-family: "Zen Maru Gothic", sans-serif;
    color: var(--ink);
  }
  .lead {
    position: absolute; left: 138px; top: 44px;
    font-family: "M PLUS 1p", sans-serif; font-weight: 800;
    font-size: 38px; letter-spacing: 2px; color: var(--muted);
    margin: 0;
  }
  .title-first {
    position: absolute; left: 512px; top: 58px;
    font-weight: 900; font-size: 100px; line-height: 1; color: var(--accent);
  }
  .title-right, .title-left {
    position: absolute; margin: 0;
    writing-mode: vertical-rl; font-weight: 900; line-height: 1;
  }
  .title-right { left: 612px; top: 58px; font-size: 100px; letter-spacing: 6px; }
  .title-left { left: 14px; top: 262px; font-size: 98px; color: var(--accent); letter-spacing: 2px; }
  .title-right .small { font-size: 60px; }
  .red { color: var(--accent); }
  .panel {
    position: absolute; left: 238px; top: 222px; width: 374px; height: 1000px;
    background: var(--panel); border-radius: 187px 187px 0 0;
  }
  .subtitle {
    position: absolute; left: 400px; top: 258px; margin: 0;
    writing-mode: vertical-rl; font-family: "M PLUS 1p", sans-serif; font-weight: 700;
    font-size: 78px; line-height: 1.1; letter-spacing: 2px;
  }
  .subtitle .no { font-size: 46px; }
  .author {
    position: absolute; left: 296px; top: 300px; margin: 0;
    writing-mode: vertical-rl; font-family: "M PLUS 1p", sans-serif; font-weight: 800;
    font-size: 48px; letter-spacing: 6px; color: #b8304f;
  }
  .author-role {
    position: absolute; left: 364px; top: 322px; margin: 0;
    writing-mode: vertical-rl; font-family: "M PLUS 1p", sans-serif; font-weight: 700;
    font-size: 26px; letter-spacing: 2px; color: var(--ink);
  }
  .portrait {
    position: absolute; left: 292px; top: 722px; width: 282px; height: 282px;
    border-radius: 50%;
    background: radial-gradient(circle at 50% 40%, var(--photo-a), var(--photo-b));
  }
</style>
</head>
<body>
<main class="cover">
  <p class="lead">響きの名手がひもとく</p>
  <h1 class="book-title">
    <span class="title-first">輝</span>
    <span class="title-right">く<span class="red">毎日</span><span class="small">を</span>つくる</span>
    <span class="title-left">心の整え方・磨き方</span>
  </h1>
  <div class="panel"></div>
  <h2 class="subtitle">ひだまり<br>トーン<span class="no">の</span><span class="red">秘密</span></h2>
  <p class="author">さとうれな</p>
  <p class="author-role">ひだまりトーンコンサルタント</p>
  <div class="portrait" role="img" aria-label="著者さとうれなの肖像写真"></div>
</main>
</body>
</html>
```